BrambleWorks business card

Looking for business card design that supports our company/software values. We have 2 logo designs at the moment but open to change if you think you can enhance the brand. Check out website www.brambleworks.com.au.

Target Market(s)

Education

Contact Information for Business Card

Name, title, mobile, email and website

Font styles to use
Sans Serif

Colors

Designer to choose colors to be used in the design.

Requirements
Must have
• BrambleWorks logo with tree and tagline on rear side with dark grey background colour

```html
<!DOCTYPE html>
<html lang="en">
<head>
<meta charset="utf-8">
<title>BrambleWorks business card</title>
<link rel="stylesheet" href="https://fonts.googleapis.com/css2?family=Open+Sans:wght@400;600;700&display=swap">
<style>
  :root {
    --page-bg: #e9e9e7;
    --card-white: #ffffff;
    --card-dark: #5e5f61;
    --ink: #3c3c3c;
    --ink-soft: #555555;
    --rule: #4a4a4a;
    --green: #5b8a3c;
    --grey-block: #5f6062;
    --white: #ffffff;
  }
  * { box-sizing: border-box; margin: 0; padding: 0; }
  html, body { width: 1200px; height: 977px; overflow: hidden; }
  body {
    background: var(--page-bg);
    font-family: "Open Sans", Arial, sans-serif;
    position: relative;
  }
  .card {
    position: absolute;
    left: 260px;
    width: 680px;
    height: 390px;
    overflow: hidden;
    box-shadow: 0 6px 18px rgba(0,0,0,0.18);
  }
  /* rear side */
  .card--back { top: 60px; background: var(--card-dark); }
  .back-brand {
    position: absolute;
    left: 0; right: 0; top: 110px;
    display: flex; flex-direction: column; align-items: center; gap: 22px;
  }
  .back-brand__dot {
    width: 86px; height: 86px; border-radius: 50%;
    background: var(--white);
  }
  .back-brand__name {
    color: var(--white); font-size: 40px; font-weight: 400; letter-spacing: 0.5px;
  }
  /* front side */
  .card--front { top: 520px; background: var(--card-white); }
  .front-brand {
    position: absolute; left: 44px; top: 58px;
    display: flex; align-items: center; gap: 14px;
  }
  .front-brand__dot {
    width: 50px; height: 50px; border-radius: 50%; background: var(--ink-soft);
  }
  .front-brand__name {
    color: var(--ink-soft); font-size: 30px; font-weight: 400; line-height: 1;
    padding-bottom: 6px; border-bottom: 1px solid var(--rule);
  }
  .front-brand__tagline {
    color: var(--ink-soft); font-size: 12px; margin-top: 4px; letter-spacing: 0.3px;
  }
  .holder {
    position: absolute; right: 50px; top: 96px; text-align: right;
  }
  .holder__name { color: var(--ink); font-size: 20px; font-weight: 700; }
  .holder__title { color: var(--ink); font-size: 12px; margin-top: 2px; }
  .address {
    position: absolute; right: 50px; top: 178px; text-align: right;
    color: var(--ink); font-size: 12px; line-height: 1.5;
  }
  .card-lines { position: absolute; inset: 0; }
  .contacts {
    position: absolute; left: 40px; top: 268px; list-style: none;
    color: var(--ink); font-size: 13px; line-height: 1;
  }
  .contacts li { display: flex; align-items: center; gap: 10px; margin-bottom: 9px; }
  .contacts svg { width: 13px; height: 13px; fill: var(--green); }
  .band-green {
    position: absolute; left: 0; bottom: 0; width: 574px; height: 30px; background: var(--green);
  }
  .band-grey {
    position: absolute; right: 0; bottom: 0; width: 92px; height: 44px; background: var(--grey-block);
  }
</style>
</head>
<body>

<section class="card card--back" aria-label="Business card rear side">
  <div class="back-brand">
    <div class="back-brand__dot"></div>
    <div class="back-brand__name">BrambleWorks</div>
  </div>
</section>

<section class="card card--front" aria-label="Business card front side">
  <div class="front-brand">
    <div class="front-brand__dot"></div>
    <div>
      <div class="front-brand__name">BrambleWorks</div>
      <div class="front-brand__tagline">Student Success Platform</div>
    </div>
  </div>

  <div class="holder">
    <div class="holder__name">Daniel Reyes</div>
    <div class="holder__title">Founder</div>
  </div>

  <svg class="card-lines" width="680" height="390" viewBox="0 0 680 390" aria-hidden="true">
    <line x1="40" y1="258" x2="430" y2="166" stroke="#4a4a4a" stroke-width="1"/>
    <line x1="430" y1="165" x2="630" y2="165" stroke="#5b8a3c" stroke-width="3"/>
  </svg>

  <div class="address">18 Harbour Lane,<br>NSW, Australia 2000</div>

  <ul class="contacts">
    <li>
      <svg viewBox="0 0 24 24"><path d="M6.6 10.8a15.1 15.1 0 0 0 6.6 6.6l2.2-2.2a1 1 0 0 1 1-.25 11.4 11.4 0 0 0 3.6.57 1 1 0 0 1 1 1V20a1 1 0 0 1-1 1A17 17 0 0 1 3 4a1 1 0 0 1 1-1h3.5a1 1 0 0 1 1 1c0 1.25.2 2.45.57 3.57a1 1 0 0 1-.25 1z"/></svg>
      02 5550 1842
    </li>
    <li>
      <svg viewBox="0 0 24 24"><path d="M2 5h20v14H2z" opacity="0"/><path d="M2 6l10 7 10-7V5H2zm0 2.4V19h20V8.4l-10 7z"/></svg>
      info@brambleworks.com.au
    </li>
    <li>
      <svg viewBox="0 0 24 24"><circle cx="12" cy="12" r="10"/></svg>
      www.brambleworks.com.au
    </li>
  </ul>

  <div class="band-green"></div>
  <div class="band-grey"></div>
</section>

</body>
</html>
```